Eye Doctor Website

We are looking for a new logo and update to our website.

The Practice Name is Dr. Helen Tarbeck and Associates

This is a simple straight forward project that requires some aspect of Optometry or eye care in the logo. Also we are located in Colorado so if we are open to the idea of adding some element of the Colorado state flag or image of the mountains

For the web all the text is already complete visit www.drhelentarbeck-example.com to see what we currently have we will be taking what you created and updating this site.

We would like the new logo to be used on the web and on business cards.

Please only submit the first page of the web site. Then we can get the rest from there.

Text does not need to be included for the design but would help.

Good luck and let us know if you have any questions

Target Market(s)

30-50 year olds looking for an eye exam.

Site must be fun but also serious and professional to catch the patients attention. Trying to play on outdoor theme

Industry/Entity Type

Flag

Font styles to use
Serif

Colors

Designer to choose colors to be used in the design.

Requirements
Must have
• Need a theme to play off of... Either use the state flag of Colorado or something with mountains. We are very close to the Rocky Mountains so this would work.

Want this them to play throughout the whole site and on Business cards
Nice to have
• Simple navigation. Don't need a lot of text
Should not have
• Clutter.... Simple to the point.

```html
<!DOCTYPE html>
<html lang="en">
<head>
<meta charset="utf-8">
<title>Dr. Helen Tarbeck and Associates</title>
<link rel="stylesheet" href="https://fonts.googleapis.com/css2?family=Montserrat:wght@400;700&family=Open+Sans:wght@400;600;700&display=swap">
<style>
:root{
  --blue:#4f8cc6;
  --blue-dark:#3b72a8;
  --navy:#2b3e55;
  --charcoal:#444649;
  --footer:#3a3b3d;
  --page:#eceff2;
  --line:#d5dadf;
  --text:#5d6166;
  --white:#ffffff;
}
*{box-sizing:border-box;margin:0;padding:0}
html,body{width:876px;height:1200px;overflow:hidden}
body{background:var(--page);font-family:"Open Sans",Arial,sans-serif;color:var(--text);position:relative}
.wrap{position:absolute;left:35px;width:806px}
.site-header{top:0;height:60px;background:var(--white);position:absolute;left:0;width:876px}
.brand{position:absolute;left:35px;top:14px;display:flex;align-items:center;gap:10px}
.brand-dot{width:36px;height:36px;border-radius:50%;background:var(--navy)}
.brand-name{font-family:"Montserrat",Arial,sans-serif;font-weight:700;color:var(--navy);font-size:15px;line-height:16px;letter-spacing:.5px}
.brand-name small{display:block;font-size:10px}
.call{position:absolute;left:470px;top:12px;font-family:"Montserrat",Arial,sans-serif}
.call span{display:block;font-size:8px;color:#8a9096;letter-spacing:1px}
.call strong{font-size:20px;color:var(--navy);font-weight:700}
.search{position:absolute;left:700px;top:22px;display:flex}
.search input{width:92px;height:20px;border:1px solid var(--line);font-size:9px;padding:0 5px;font-family:inherit}
.search button{height:20px;width:48px;background:var(--charcoal);color:#fff;border:0;font-size:8px;font-family:inherit}
.main-nav{top:62px;height:28px;background:var(--charcoal);display:flex}
.main-nav a{color:#fff;text-decoration:none;font-family:"Montserrat",Arial,sans-serif;font-size:9.5px;letter-spacing:.5px;padding:0 14px;line-height:28px;border-right:1px solid #5a5c60}
.main-nav a.active{background:var(--blue)}
.hero{top:96px;height:270px;background:linear-gradient(180deg,#6f9cc6 0%,#a9c2d8 38%,#e7ecf0 55%,#7b848d 80%,#3f474f 100%)}
.hero-box{position:absolute;left:155px;top:62px;width:200px;background:rgba(255,255,255,.92);padding:12px 14px}
.hero-box h1{font-family:"Montserrat",Arial,sans-serif;font-weight:400;font-size:16px;color:var(--navy);margin-bottom:6px}
.hero-box p{font-size:8.5px;line-height:12px}
.hero-box p b{color:var(--blue)}
.dots{position:absolute;bottom:10px;left:50%;transform:translateX(-50%);display:flex;gap:5px}
.dots i{width:7px;height:7px;border-radius:50%;background:#fff;opacity:.6}
.dots i:first-child{opacity:1;background:var(--blue)}
.features{top:380px;display:flex;gap:18px}
.feature{width:188px;height:230px;background:var(--white);border:1px solid var(--line);text-align:center;padding:24px 16px}
.feature.dark{background:var(--charcoal);color:#e4e6e8;border-color:var(--charcoal)}
.feature svg{width:40px;height:40px}
.feature h3{font-family:"Montserrat",Arial,sans-serif;font-weight:400;font-size:12px;color:var(--navy);margin:14px 0 8px}
.feature.dark h3{color:#fff}
.feature p{font-size:8.5px;line-height:12px}
.feature .more{display:inline-block;margin-top:22px;font-size:8px;padding:4px 10px;border:1px solid var(--line);color:var(--navy)}
.feature.dark .more{background:var(--blue);border-color:var(--blue);color:#fff}
.section-title{font-family:"Montserrat",Arial,sans-serif;font-size:15px;color:var(--navy);font-weight:400}
.section-title b{color:var(--blue)}
.care-title{top:626px;width:806px;border-bottom:1px solid var(--line);padding-bottom:6px}
.gallery{top:656px;display:flex;gap:15px}
.gallery figure{width:190px}
.photo{height:110px}
.gallery figcaption{text-align:center;padding-top:8px}
.gallery h4{font-family:"Montserrat",Arial,sans-serif;font-weight:400;font-size:13px;color:var(--navy)}
.gallery p{font-size:8px;line-height:11px;margin-top:3px}
.services{top:838px;width:410px}
.services .section-title{border-bottom:1px solid var(--line);padding-bottom:6px;margin-bottom:10px}
.services .lead{font-size:10px;color:var(--navy);margin-bottom:8px}
.services .lead b{color:var(--blue)}
.services ul{list-style:none}
.services li{font-size:9px;line-height:13px;margin-bottom:5px;padding-left:16px;position:relative}
.services li svg{position:absolute;left:0;top:2px;width:9px;height:9px}
.contact-box{top:852px;left:475px;width:366px;height:185px;background:linear-gradient(180deg,#5d97cf,#3f78b0);padding:12px 16px;color:#fff}
.contact-box h3{font-family:"Montserrat",Arial,sans-serif;font-weight:700;font-size:11px;letter-spacing:1px}
.contact-box p{font-size:7.5px;opacity:.85;margin-bottom:8px}
.contact-box label{display:block;font-size:8px;margin-top:4px}
.contact-box .field{height:16px;background:rgba(255,255,255,.92);margin-top:2px}
.contact-box .field.msg{height:34px}
.contact-box .send{position:absolute;right:16px;bottom:10px;background:var(--charcoal);font-size:8px;padding:3px 12px}
.site-footer{position:absolute;left:0;top:1058px;width:876px;height:142px;background:var(--footer);color:#b9bcc0}
.site-footer h5{font-family:"Montserrat",Arial,sans-serif;font-weight:400;font-size:9px;color:#fff;letter-spacing:1px;margin-bottom:7px}
.fcol{position:absolute;top:16px;font-size:7.5px;line-height:11px}
.fcol.nav{left:35px}
.fcol.company{left:330px}
.fcol.company b{color:#fff}
.fcol.location{left:625px;width:216px}
.map{height:96px;background:linear-gradient(135deg,#e6e8e3,#cfd6d9)}
.copy{position:absolute;left:35px;bottom:10px;font-size:6.5px;color:#888}
</style>
</head>
<body>
<header class="site-header">
  <div class="brand"><span class="brand-dot"></span><div class="brand-name">DR. HELEN TARBECK<small>AND ASSOCIATES</small></div></div>
  <div class="call"><span>CALL US TODAY</span><strong>+1-555-0142-3390</strong></div>
  <form class="search"><input type="text" placeholder="Search"><button type="button">SEARCH</button></form>
</header>

<nav class="wrap main-nav">
  <a class="active" href="#">WELCOME</a><a href="#">DR TARBECK</a><a href="#">SCHEDULE AN APPOINTMENT</a><a href="#">OFFICE INFO/SPECIALS</a><a href="#">CONTACT US</a>
</nav>

<section class="wrap hero" role="img" aria-label="Snow-capped Rocky Mountain peaks under a blue sky">
  <div class="hero-box">
    <h1>Aenean vulputate eleifend</h1>
    <p>Donec pede justo, fringilla vel, aliquet nec, vulputate eget arcu. In enim justo, rhoncus ut, imperdiet a, <b>venenatis vitae, justo.</b></p>
  </div>
  <div class="dots"><i></i><i></i><i></i></div>
</section>

<section class="wrap features">
  <article class="feature"><svg viewBox="0 0 40 40"><circle cx="20" cy="20" r="19" fill="var(--blue)"/><path d="M10 20c3-5 7-7 10-7s7 2 10 7c-3 5-7 7-10 7s-7-2-10-7z" fill="#fff"/><circle cx="20" cy="20" r="3.5" fill="var(--blue)"/></svg><h3>Pretium quis, sem</h3><p>Donec pede justo, fringilla vel, aliquet nec, vulputate eget, arcu. In enim justo, rhoncus ut imperdiet a venenatis vitae.</p><span class="more">Read More</span></article>
  <article class="feature"><svg viewBox="0 0 40 40"><circle cx="20" cy="20" r="19" fill="var(--blue)"/><circle cx="20" cy="16" r="5" fill="#fff"/><path d="M11 30c1-6 5-8 9-8s8 2 9 8z" fill="#fff"/></svg><h3>Nullam dictum felis</h3><p>Donec pede justo, fringilla vel, aliquet nec, vulputate eget, arcu. In enim justo, rhoncus ut imperdiet a venenatis vitae.</p><span class="more">Read More</span></article>
  <article class="feature dark"><svg viewBox="0 0 40 40"><circle cx="20" cy="20" r="19" fill="var(--blue)"/><rect x="11" y="12" width="18" height="16" rx="2" fill="#fff"/><path d="M11 16h18" stroke="var(--blue)" stroke-width="2"/></svg><h3>Nullam dictum felis</h3><p>Donec pede justo, fringilla vel, aliquet nec, vulputate eget, arcu. In enim justo, rhoncus ut imperdiet a venenatis vitae.</p><span class="more">Read More</span></article>
  <article class="feature"><svg viewBox="0 0 40 40"><circle cx="20" cy="20" r="19" fill="var(--blue)"/><path d="M10 20c3-5 7-7 10-7s7 2 10 7c-3 5-7 7-10 7s-7-2-10-7z" fill="#fff"/><circle cx="20" cy="20" r="3.5" fill="var(--blue)"/></svg><h3>Nullam dictum felis</h3><p>Donec pede justo, fringilla vel, aliquet nec, vulputate eget, arcu. In enim justo, rhoncus ut imperdiet a venenatis vitae.</p><span class="more">Read More</span></article>
</section>

<h2 class="wrap section-title care-title">We are here to provide you <b>thorough eye care</b></h2>

<section class="wrap gallery">
  <figure><div class="photo" role="img" aria-label="Eye close-up" style="background:linear-gradient(135deg,#c9a98e,#6f7f8c)"></div><figcaption><h4>Company Motto</h4><p>In enim justo, rhoncus ut imperdiet a, venenatis vitae justo nullam dictum.</p></figcaption></figure>
  <figure><div class="photo" role="img" aria-label="Colorado mountain landscape" style="background:linear-gradient(180deg,#7ea7cf,#d9e1e6 55%,#8a6d55)"></div><figcaption><h4>Company Location</h4><p>In enim justo, rhoncus ut imperdiet a, venenatis vitae justo nullam dictum.</p></figcaption></figure>
  <figure><div class="photo" role="img" aria-label="Eye chart in exam room" style="background:linear-gradient(135deg,#f2f2f0,#b9bcbe)"></div><figcaption><h4>Company Service</h4><p>In enim justo, rhoncus ut imperdiet a, venenatis vitae justo nullam dictum.</p></figcaption></figure>
  <figure><div class="photo" role="img" aria-label="Pair of eyeglasses" style="background:linear-gradient(135deg,#9aa3ab,#2f3337)"></div><figcaption><h4>Best Equipment</h4><p>In enim justo, rhoncus ut imperdiet a, venenatis vitae justo nullam dictum.</p></figcaption></figure>
</section>

<section class="wrap services">
  <h2 class="section-title"><b>Services</b> we provide</h2>
  <p class="lead">Contact us for a complete listing <b>+1-555-0142-3390</b></p>
  <ul>
    <li><svg viewBox="0 0 10 10"><path d="M1 5l3 3 5-7" fill="none" stroke="var(--blue)" stroke-width="2"/></svg>Comprehensive eye exams with testing for glaucoma, cataracts, and macular degeneration</li>
    <li><svg viewBox="0 0 10 10"><path d="M1 5l3 3 5-7" fill="none" stroke="var(--blue)" stroke-width="2"/></svg>Contact lens exams including astigmatism toric, bifocal and gas permeable lenses</li>
    <li><svg viewBox="0 0 10 10"><path d="M1 5l3 3 5-7" fill="none" stroke="var(--blue)" stroke-width="2"/></svg>Treatment of eye infections, dry eyes and other eye problems</li>
    <li><svg viewBox="0 0 10 10"><path d="M1 5l3 3 5-7" fill="none" stroke="var(--blue)" stroke-width="2"/></svg>Diabetic eye exams</li>
    <li><svg viewBox="0 0 10 10"><path d="M1 5l3 3 5-7" fill="none" stroke="var(--blue)" stroke-width="2"/></svg>Pediatric eye exams</li>
  </ul>
</section>

<form class="wrap contact-box">
  <h3>CONTACT US</h3>
  <p>We respond to all inquiries within one business day.</p>
  <label>Name</label><div class="field"></div>
  <label>Email</label><div class="field"></div>
  <label>Message</label><div class="field msg"></div>
  <span class="send">SUBMIT</span>
</form>

<footer class="site-footer">
  <div class="fcol nav"><h5>QUICK NAVIGATION</h5>Welcome<br>Dr. Tarbeck<br>Schedule an Appointment<br>Office Info/Specials<br>Contact Us<br>Privacy Policy</div>
  <div class="fcol company"><h5>OUR COMPANY</h5><b>Dr. Helen Tarbeck and Associates</b><br>1420 Aspen Ridge Parkway, Lakewood, CO 80000<br>(555) 014-7788<br><br><b>Visit us Weekdays:</b><br>Monday: 10:00am - 6:00pm<br>Wednesday: 10:00am - 7:00pm<br>Thursday: 9:00am - 5:00pm</div>
  <div class="fcol location"><h5>OUR LOCATION</h5><div class="map" role="img" aria-label="Street map of the office location"></div></div>
  <div class="copy">Copyright © Dr. Helen Tarbeck and Associates. All rights reserved.</div>
</footer>
</body>
</html>
```